Martial Arts Website

Redevelopment of existing martial arts website.

The academy teaches traditional shaolin martial arts, including Shaolin Kung Fu, Wu Shu, Tai Chi, Qigong and Wing Chun and the site needs to reflect the traditional roots (eg, no tacky boxing imagery)

Existing website is www.copperheron.com.au to get a feel for the desired color scheme (black, green and red). The exact colors can be tweaked though. Please only reuse the logo and font (Karate) - there isnt anything else from the current design that needs to remain.

The current website includes links to a YouTube channel that includes demonstrations of the training conducted to better guide the design.

The new website site map will be:
1. Home
2. Programs - summary page describing each form of training
a. Tiny Otters
b. Kids Kung Fu
c. Youth Kung Fu
d. Adults Kung Fu
e. Wing Chun
f. Tai Chi & Qigong
g. Weaponry Classes
h. 72 Arts of Shaolin Conditioning Program
i. Acrobatics and Wu Shu
j. Fitness Boxing
3. Timetable
4. Coaches - summary page describing all coaches
a. Sifu (Master)
b. Sihing Lou
c. Sihing Kim
d. Sihing Felix
X. ... up to 10 or so coaches
5. Member Zone
6. Contact Us
Updates

Logo now attached to brief - sorry I only have it in PDF

Just to clarify, I am only expecting a PSD design - no HTML required

Reason: Thanks for the designs, we love a lot of them just require a little extra time to tweak the designs and establish the potential. Thanks for your understanding and efforts.

Target Market(s)

Parents, teenagers, young adults, adults, elderly

Industry/Entity Type

Training

Requirements
Must have
• Chinese kung fu dragon imagery throughout the background
Links to Facebook and YouTube channel
Promo/icon in the header "Try 2 free classes now"
Home page should include an embedded YouTube video

```html
<!DOCTYPE html>
<html lang="en">
<head>
<meta charset="utf-8">
<title>Copper Heron Martial Arts Academy – Contact Us</title>
<link href="https://fonts.googleapis.com/css2?family=Marcellus&family=Ubuntu:wght@400;500&family=PT+Sans:wght@400;700&display=swap" rel="stylesheet">
<style>
:root{
  --bg-green-top:#1f6d14;
  --bg-green-bottom:#2c8a1c;
  --panel:#000;
  --nav-top:#3cb81e;
  --nav-bottom:#1c8a0c;
  --nav-text:#0a2a04;
  --tab:#0c5a06;
  --tab-text:#86e864;
  --accent:#27a513;
  --text-muted:#a9a9a9;
  --text-light:#e6e6e6;
  --divider:#2a2a2a;
  --button:#1d6e10;
}
*{margin:0;padding:0;box-sizing:border-box}
html,body{width:1033px;height:1200px;overflow:hidden}
body{position:relative;background:linear-gradient(180deg,var(--bg-green-top),var(--bg-green-bottom) 70%);font-family:'PT Sans',sans-serif}
.abs{position:absolute}

.site-title{font-family:'Marcellus',serif;font-size:25px;color:#fff;top:50px}
.site-title.left{left:205px}
.site-title.right{left:579px}

.page{left:15px;top:107px;width:995px;height:843px;background:var(--panel);border-radius:6px 6px 0 0}

.nav{left:25px;top:115px;width:972px;height:65px;border-radius:6px;background:linear-gradient(180deg,var(--nav-top),var(--nav-bottom))}
.nav-item{font-family:'Ubuntu',sans-serif;color:var(--nav-text);text-transform:uppercase}
.nav-item.main{font-size:16px;top:141px}
.nav-item.sub{font-size:13px;top:143px}
.nav-tab{left:139px;top:125px;width:117px;height:60px;background:var(--tab);border-radius:8px 8px 0 0}
.nav-item.active{color:var(--tab-text)}

.logo-badge{left:400px;top:20px;width:176px;height:176px;border-radius:50%;background:radial-gradient(circle,#000 62%,#1a5e0e 64%,#5fd43a 80%,#1d7a10 100%);display:flex;align-items:center;justify-content:center}
.logo-badge span{font-family:'Marcellus',serif;color:#fff;font-size:18px;text-align:center;line-height:1.2}

.hero{left:27px;top:184px;width:969px;height:359px;background:linear-gradient(180deg,#8a6d4f 0%,#c9c3bb 35%,#b7826e 70%,#c8705a 100%)}

.dropdown{left:140px;top:176px;width:259px;height:130px;background:var(--tab);border-radius:0 6px 8px 8px}
.dropdown a{position:absolute;font-family:'Ubuntu',sans-serif;font-size:13px;color:var(--tab-text);text-decoration:none}

.content{left:27px;top:543px;width:969px;height:396px;border:1px solid #15530c;border-top:none;border-radius:0 0 6px 6px}
.section-title{left:46px;top:568px;font-family:'Ubuntu',sans-serif;font-size:17px;color:var(--accent)}
.form-heading{left:54px;top:615px;font-size:18px;color:var(--text-muted)}
.field-label{left:54px;font-size:12px;color:var(--text-muted)}
.field{left:54px;width:245px;height:21px;background:#fff;border:1px solid #ccc}
.field.comment{height:47px}
.submit{left:94px;top:888px;width:154px;height:24px;border-radius:5px;background:var(--button);color:#fff;font-weight:700;font-size:13px;text-align:center;line-height:24px}
.divider{left:463px;top:625px;width:1px;height:313px;background:var(--divider)}
.map{left:485px;top:641px;width:253px;height:252px;background:linear-gradient(135deg,#e4e0d8,#d8d4cc 60%,#ece6c4)}

.contact-icon{left:772px;top:761px}
.contact-heading{left:810px;top:764px;font-size:18px;color:#8d8d8d}
.contact-line{left:777px;font-size:11px;color:#9a9a9a}

.footer{left:0;top:950px;width:1033px;height:250px;background:#000}
.footer-link{font-size:12.5px;color:var(--text-light);padding-left:15px}
.footer-link::before{content:"";position:absolute;left:0;top:4px;border-left:5px solid #9a9a9a;border-top:4px solid transparent;border-bottom:4px solid transparent}
.footer-badge{left:785px;top:967px;width:120px;height:120px;border-radius:50%;background:radial-gradient(circle,#000 62%,#1a5e0e 64%,#5fd43a 80%,#1d7a10 100%);display:flex;align-items:center;justify-content:center}
.footer-badge span{font-family:'Marcellus',serif;color:#fff;font-size:13px;text-align:center;line-height:1.2}
.copyright{left:48px;top:1130px;font-size:12px;color:#a0a0a0}
</style>
</head>
<body>
  <header>
    <div class="abs site-title left">Copper Heron</div>
    <div class="abs site-title right">Martial Arts Academy</div>
  </header>

  <div class="abs page"></div>

  <nav>
    <div class="abs nav"></div>
    <div class="abs nav-tab"></div>
    <span class="abs nav-item main" style="left:76px">Home</span>
    <span class="abs nav-item main active" style="left:159px">Programs</span>
    <span class="abs nav-item main" style="left:274px">Timetable</span>
    <span class="abs nav-item sub" style="left:633px">Coaches</span>
    <span class="abs nav-item sub" style="left:722px">Member Zone</span>
    <span class="abs nav-item sub" style="left:849px">Contact Us</span>
  </nav>

  <div class="abs logo-badge"><span>Copper<br>Heron</span></div>

  <div class="abs hero" role="img" aria-label="Photo of a kung fu master leading a tai chi class in a sports hall"></div>

  <div class="abs dropdown">
    <a style="left:20px;top:13px">Tiny Otters</a>
    <a style="left:20px;top:40px">Kids Kung Fu</a>
    <a style="left:20px;top:67px">Youth Kung Fu</a>
    <a style="left:20px;top:94px">Adults Kung Fu</a>
    <a style="left:132px;top:13px">Wing Chun</a>
    <a style="left:132px;top:40px">Tai Chi &amp; Qigong</a>
    <a style="left:132px;top:67px">Weaponry Classes</a>
    <a style="left:132px;top:94px">72 Arts of Shaolin</a>
  </div>

  <main>
    <div class="abs content"></div>
    <h1 class="abs section-title" style="font-weight:400">Contact Us</h1>
    <h2 class="abs form-heading" style="font-weight:400">Kindly post your valuable Suggestions &amp; Query</h2>

    <label class="abs field-label" style="top:657px">Enter your Name</label>
    <div class="abs field" style="top:676px"></div>
    <label class="abs field-label" style="top:705px">Enter your Email</label>
    <div class="abs field" style="top:726px"></div>
    <label class="abs field-label" style="top:753px">Enter your Phone Number</label>
    <div class="abs field" style="top:776px"></div>
    <label class="abs field-label" style="top:801px">Add Your Comments Here:</label>
    <div class="abs field comment" style="top:818px"></div>
    <div class="abs submit">Submit Query</div>

    <div class="abs divider"></div>
    <div class="abs map" role="img" aria-label="Street map showing the academy location"></div>

    <svg class="abs contact-icon" width="26" height="26" viewBox="0 0 26 26" aria-hidden="true">
      <rect width="26" height="26" rx="4" fill="#3a3a3a"/>
      <path d="M9 6 L12 9 L10.5 11 Q12 14.5 15 15.5 L17 14 L20 17 L18 20 Q9 19 6 9 Z" fill="#9a9a9a"/>
    </svg>
    <div class="abs contact-heading">Contact Details</div>
    <div class="abs contact-line" style="top:803px">#12 Harbour Road, Lorem ipsum,</div>
    <div class="abs contact-line" style="top:827px">Phone: +91 804123570</div>
    <div class="abs contact-line" style="top:851px">Tollfree: (006) 60918243</div>
    <div class="abs contact-line" style="top:875px">E-mail: info@copperheron.com.au</div>
  </main>

  <footer>
    <div class="abs footer"></div>
    <span class="abs footer-link" style="left:48px;top:977px">Home</span>
    <span class="abs footer-link" style="left:48px;top:1007px">Programs</span>
    <span class="abs footer-link" style="left:48px;top:1037px">Timtable</span>
    <span class="abs footer-link" style="left:48px;top:1067px">Coaches</span>

    <span class="abs footer-link" style="left:167px;top:978px">Support</span>
    <span class="abs footer-link" style="left:167px;top:1008px">FAQ</span>
    <span class="abs footer-link" style="left:167px;top:1038px">Newslettes</span>
    <span class="abs footer-link" style="left:167px;top:1068px">Social Media</span>

    <span class="abs footer-link" style="left:302px;top:978px">Tiny Otters</span>
    <span class="abs footer-link" style="left:302px;top:1008px">Kids Kung Fu</span>
    <span class="abs footer-link" style="left:302px;top:1038px">Youth Kung Fu</span>
    <span class="abs footer-link" style="left:302px;top:1068px">Adults Kung Fu</span>

    <span class="abs footer-link" style="left:458px;top:979px">Wing Chun</span>
    <span class="abs footer-link" style="left:458px;top:1009px">Tai Chi &amp; Qigong</span>
    <span class="abs footer-link" style="left:458px;top:1039px">Weaponry Classes</span>
    <span class="abs footer-link" style="left:458px;top:1069px">72 Arts of Shaolin</span>

    <div class="abs footer-badge"><span>Copper<br>Heron</span></div>
    <div class="abs copyright">© 2012 Company Name &nbsp;|&nbsp; All right reserved</div>
  </footer>
</body>
</html>
```